Greeting Cards for all Occasions

We are a large church and are sending cards all the time for different occasions. We'd like to have 5 different cards designed that fit with our brand guidelines and logo (Attached). We'd like to have designs for the following 5x7 cards. Each title should be featured on the front, and the inside should be blank, with the back should feature the contact info below. Appropriate photos from Unsplash are welcomed.

1. Happy Birthday
2. Get Well Soon
3. Praying for You
4. Happy Anniversary
5. Thank You

Contact info to include on the back:
Millbrook Chapel
4817 Tamsin Avenue, Corona, CA 92807
www.MillbrookChapel.com I 909-418-5502

```html
<!DOCTYPE html>
<html lang="en">
<head>
<meta charset="utf-8">
<title>Happy Birthday Card – Front</title>
<link href="https://fonts.googleapis.com/css2?family=Montserrat:wght@600;700&display=swap" rel="stylesheet">
<style>
  :root {
    --card-bg: #0c0908;
    --ink: #ffffff;
    --photo-dark: #0a0706;
    --photo-warm: #3a2414;
    --photo-glow: #8a5a2c;
    --frame: #f2f2f2;
  }
  * { margin: 0; padding: 0; box-sizing: border-box; }
  html, body {
    width: 794px;
    height: 1200px;
    overflow: hidden;
    background: var(--card-bg);
  }
  .card {
    position: relative;
    width: 794px;
    height: 1200px;
    background: var(--card-bg);
    overflow: hidden;
    font-family: "Montserrat", Arial, sans-serif;
    color: var(--ink);
  }
  .cake-photo {
    position: absolute;
    left: 0;
    top: 571px;
    width: 794px;
    height: 629px;
    background:
      radial-gradient(ellipse 55% 22% at 50% 25%, rgba(255, 196, 110, 0.45), transparent 70%),
      radial-gradient(ellipse 70% 40% at 50% 62%, var(--photo-warm), transparent 75%),
      radial-gradient(ellipse 80% 25% at 45% 92%, var(--photo-glow), transparent 70%),
      var(--photo-dark);
  }
  .frame {
    position: absolute;
    left: 66px;
    top: 40px;
    width: 672px;
    height: 1109px;
    border: 4px solid var(--frame);
  }
  .brand {
    position: absolute;
    left: 86px;
    top: 90px;
    display: flex;
    align-items: center;
    gap: 12px;
    font-weight: 700;
    font-size: 26px;
    letter-spacing: 3px;
    text-transform: uppercase;
    color: var(--ink);
  }
  .brand-mark {
    width: 22px;
    height: 22px;
    background: var(--ink);
  }
  .title {
    position: absolute;
    left: 104px;
    top: 296px;
    font-weight: 700;
    font-size: 104px;
    line-height: 134px;
    letter-spacing: 1px;
    text-transform: uppercase;
    color: var(--ink);
  }
</style>
</head>
<body>
  <main class="card">
    <div class="cake-photo" role="img" aria-label="Photo of a chocolate birthday cake lit by colourful letter candles spelling happy birthday"></div>
    <div class="frame"></div>
    <div class="brand">
      <span class="brand-mark"></span>
      <span class="brand-name">Millbrook Chapel</span>
    </div>
    <h1 class="title">Happy<br>Birthday</h1>
  </main>
</body>
</html>
```